Book Cover Design Project

I have written a booK called "keep the lamp Lit:
a guide to starting and running a small business. It is aimed at the start up entrepreneur and seeks to give them everything they need to start up and run a small business. I am interested in a very simple cover that is contemporary in the look but clearly communicates the mission of the book. It should sell very well as there are no others like it, so the designer will get excellent exposure.
Updates

Reason: I an vacation in Europe until the 23rd of July. Would like a few days to make a decision after my return Walt

We are currently on vacation.  Will make a final decision in about a week.  Thanks so much for your submissions

Walt

Target Market(s)

Start up businesses in the U.S.

Industry/Entity Type

Business

Requirements
Must have
• Clear communication of the name. Lots of white space. Graphic communication of the purpose of the book? Prominent exposure of my name. Walter j. Pennick

```html
<!DOCTYPE html>
<html lang="en">
<head>
<meta charset="utf-8">
<title>Keep the Lamp Lit – Book Cover</title>
<link rel="stylesheet" href="https://fonts.googleapis.com/css2?family=Barlow+Semi+Condensed:wght@700&family=Tinos:ital,wght@0,400;0,700;1,700&display=swap">
<style>
  :root {
    --page-bg: #f7f9fa;
    --paper: #ffffff;
    --ink: #000000;
    --accent: #fb5a26;
    --accent-heading: #f04a23;
    --crop-mark: #e2e4e4;
    --fold-line: #f1f2f2;
    --frame: #dcdcdc;
  }
  * { margin: 0; padding: 0; box-sizing: border-box; }
  html, body {
    width: 1200px;
    height: 900px;
    overflow: hidden;
    background: var(--page-bg);
  }
  .canvas {
    position: relative;
    width: 1200px;
    height: 900px;
  }
  .crop-marks {
    position: absolute;
    inset: 0;
  }
  .cover-sheet {
    position: absolute;
    left: 138px;
    top: 125px;
    width: 924px;
    height: 648px;
    background: var(--paper);
  }
  .spine-fold {
    position: absolute;
    top: 0;
    width: 1px;
    height: 100%;
    background: var(--fold-line);
  }
  .spine-fold--left { left: 434px; }
  .spine-fold--right { left: 490px; }

  /* Back cover */
  .back-blurb {
    position: absolute;
    left: 100px;
    top: 172px;
    width: 235px;
    font-family: 'Tinos', 'Times New Roman', serif;
    color: var(--ink);
  }
  .back-blurb__heading {
    font-size: 21px;
    font-weight: 700;
    color: var(--accent-heading);
    text-align: center;
    line-height: 26px;
    margin-bottom: 5px;
  }
  .back-blurb__text {
    font-size: 13.4px;
    line-height: 17.3px;
    text-align: justify;
    hyphens: manual;
  }

  /* Spine */
  .spine-text {
    position: absolute;
    left: 460px;
    width: 0;
    display: flex;
    justify-content: center;
    align-items: center;
    white-space: nowrap;
  }
  .spine-text span {
    transform: rotate(-90deg);
    display: block;
  }
  .spine-text--author {
    top: 140px;
    height: 192px;
    font-family: 'Tinos', 'Times New Roman', serif;
    font-weight: 700;
    font-size: 19px;
  }
  .spine-text--title {
    top: 372px;
    height: 135px;
    font-family: 'Barlow Semi Condensed', 'Arial Narrow', sans-serif;
    font-weight: 700;
    font-size: 20px;
    letter-spacing: 0.3px;
  }

  /* Front cover */
  .front-title {
    position: absolute;
    left: 490px;
    width: 434px;
    top: 203px;
    text-align: center;
    font-family: 'Barlow Semi Condensed', 'Arial Narrow', sans-serif;
    font-weight: 700;
    font-size: 38px;
    line-height: 46px;
    letter-spacing: 0.4px;
    color: var(--ink);
  }
  .front-title__accent { color: var(--accent); }

  .framed-box {
    position: absolute;
    border: 6px solid var(--frame);
    background: var(--paper);
    text-align: center;
    font-family: 'Tinos', 'Times New Roman', serif;
  }
  .subtitle {
    left: 601px;
    top: 270px;
    width: 211px;
    height: 56px;
    font-size: 17px;
    line-height: 21px;
    padding-top: 2px;
    color: var(--ink);
  }
  .subtitle__accent { color: var(--accent); }
  .subtitle__keyword { color: var(--accent); font-weight: 700; font-style: italic; }

  .front-author {
    left: 585px;
    top: 564px;
    width: 243px;
    height: 35px;
    font-size: 21px;
    font-weight: 700;
    line-height: 23px;
    color: var(--ink);
    white-space: nowrap;
  }
</style>
</head>
<body>
<main class="canvas">
  <svg class="crop-marks" width="1200" height="900" aria-hidden="true">
    <g stroke="var(--crop-mark)" stroke-width="3" fill="none">
      <path d="M121 125h34M138 108v34"/>
      <path d="M555 125h34M572 108v34"/>
      <path d="M611 125h34M628 108v34"/>
      <path d="M1045 125h34M1062 108v34"/>
      <path d="M121 773h34M138 756v34"/>
      <path d="M555 773h34M572 756v34"/>
      <path d="M611 773h34M628 756v34"/>
      <path d="M1045 773h34M1062 756v34"/>
    </g>
  </svg>

  <section class="cover-sheet">
    <div class="spine-fold spine-fold--left"></div>
    <div class="spine-fold spine-fold--right"></div>

    <article class="back-blurb">
      <h2 class="back-blurb__heading">Lorem Ipsum Dolor</h2>
      <p class="back-blurb__text">Lorem ipsum dolor sit amet, consec&shy;tetuer adipiscing elit, sed diam non&shy;ummy nibh euismod tincidunt ut laoreet dolore magna aliquam erat volutpat. Ut wisi enim ad minim veniam, quis nos&shy;trud exerci tation ullamcorper suscipit lobortis nisl ut aliquip ex ea commodo consequat. Duis autem vel eum iriure dolor in hendrerit in vulputate velit esse</p>
    </article>

    <div class="spine-text spine-text--author"><span>Walter J. Pennick</span></div>
    <div class="spine-text spine-text--title"><span>KEEP THE LAMP LIT</span></div>

    <h1 class="front-title">KEEP THE <span class="front-title__accent">LAMP LIT</span></h1>

    <p class="framed-box subtitle">a guide for <span class="subtitle__keyword">starting</span> <span class="subtitle__accent">and</span><br><span class="subtitle__keyword">running</span> <span class="subtitle__accent">small business</span></p>

    <p class="framed-box front-author">Walter J. Pennick</p>
  </section>
</main>
</body>
</html>
```